Business Card Design Project

Personal Service. There are three areas of my service: Resourceful/Recycling Consultation, Life Coaching using Law of Attraction & Visualization Board. My current cards has: Visualization to Manifestation. I would like to work with this theme

Industry/Entity Type

Business

Contact Information for Business Card

Circles. Recyling Triangle

```html
<!DOCTYPE html>
<html lang="en">
<head>
<meta charset="utf-8">
<title>Loopwell Business Card</title>
<link rel="stylesheet" href="https://fonts.googleapis.com/css2?family=Montserrat:wght@300;400;500;600&display=swap">
<style>
  :root {
    --backdrop: #ece7e0;
    --teal: #12a89d;
    --purple: #47276e;
    --lime: #8dc63f;
    --white: #ffffff;
    --font: "Montserrat", Arial, sans-serif;
  }
  * { margin: 0; padding: 0; box-sizing: border-box; }
  html, body {
    width: 1200px;
    height: 964px;
    overflow: hidden;
    background: var(--backdrop);
    font-family: var(--font);
  }
  .canvas { position: relative; width: 1200px; height: 964px; }
  .card {
    position: absolute;
    top: 122px;
    width: 408px;
    height: 686px;
    overflow: hidden;
  }
  .card-front { left: 157px; background: var(--teal); color: var(--white); }
  .card-back { left: 618px; background: var(--purple); color: var(--white); }

  /* Front */
  .brand {
    position: absolute;
    top: 50px;
    left: 0;
    width: 100%;
    text-align: center;
    color: var(--purple);
    font-weight: 300;
    line-height: 1;
  }
  .brand-name { display: block; font-size: 52px; letter-spacing: 1px; }
  .brand-line { display: block; font-size: 19px; letter-spacing: 1px; margin-top: 8px; text-transform: uppercase; }
  .pattern-band {
    position: absolute;
    left: 0;
    top: 170px;
    width: 100%;
    height: 184px;
    background: radial-gradient(closest-side, rgba(71,39,110,0.38) 0%, rgba(71,39,110,0.14) 55%, rgba(71,39,110,0) 100%);
  }
  .service {
    position: absolute;
    left: 0;
    width: 100%;
    text-align: center;
    font-size: 20px;
    font-weight: 400;
    line-height: 31px;
  }
  .service-title { font-weight: 600; font-size: 23px; }
  .service-title::before {
    content: "";
    display: inline-block;
    width: 14px;
    height: 14px;
    border-radius: 50%;
    background: var(--lime);
    margin-right: 12px;
    vertical-align: 2px;
  }
  .service-recycling { top: 410px; }
  .service-recycling .service-title::before { margin-right: 18px; margin-left: -36px; }
  .service-coaching { top: 509px; }

  /* Back */
  .person { position: absolute; left: 56px; top: 56px; }
  .person-name { font-size: 31px; font-weight: 400; color: var(--lime); line-height: 1.1; }
  .person-role { font-size: 14px; font-weight: 500; color: var(--teal); margin-top: 2px; }
  .contact { position: absolute; left: 56px; top: 120px; list-style: none; }
  .contact li {
    display: flex;
    align-items: center;
    font-size: 18px;
    font-weight: 500;
    height: 35px;
  }
  .contact svg { width: 17px; height: 17px; margin-right: 10px; }
  .pattern-side {
    position: absolute;
    left: 0;
    top: 327px;
    width: 300px;
    height: 186px;
    background: radial-gradient(closest-side at 50% 50%, rgba(18,168,157,0.5) 0%, rgba(18,168,157,0.18) 55%, rgba(18,168,157,0) 100%);
  }
  .tagline {
    position: absolute;
    top: 554px;
    left: 0;
    width: 100%;
    text-align: center;
    font-size: 21px;
    font-weight: 400;
  }
  .website {
    position: absolute;
    top: 589px;
    left: 0;
    width: 100%;
    text-align: center;
    font-size: 20px;
    font-weight: 600;
    color: var(--teal);
  }
</style>
</head>
<body>
<main class="canvas">
  <section class="card card-front">
    <h1 class="brand">
      <span class="brand-name">LOOPWELL.</span>
      <span class="brand-line">Renewal Studio</span>
    </h1>
    <div class="pattern-band" role="img" aria-label="Decorative band of overlapping outlined circles"></div>
    <div class="service service-recycling">
      <div class="service-title">Resourceful/Recycling</div>
      <div>Consultation</div>
    </div>
    <div class="service service-coaching">
      <div class="service-title">Life Coaching</div>
      <div>using Law of Attraction</div>
      <div>&amp; Visualization Board</div>
    </div>
  </section>

  <section class="card card-back">
    <div class="person">
      <div class="person-name">John Doe</div>
      <div class="person-role">Consultant</div>
    </div>
    <ul class="contact">
      <li>
        <svg viewBox="0 0 24 24" aria-hidden="true"><path fill="var(--teal)" d="M6.6 10.8a15.1 15.1 0 0 0 6.6 6.6l2.2-2.2c.3-.3.7-.4 1-.2 1.1.4 2.3.6 3.6.6.6 0 1 .4 1 1V20c0 .6-.4 1-1 1A17 17 0 0 1 3 4c0-.6.4-1 1-1h3.5c.6 0 1 .4 1 1 0 1.3.2 2.5.6 3.6.1.3 0 .7-.2 1z"/></svg>
        01245387
      </li>
      <li>
        <svg viewBox="0 0 24 24" aria-hidden="true"><rect x="2" y="5" width="20" height="14" fill="var(--teal)"/><path d="M3 6l9 6.3L21 6" fill="none" stroke="var(--purple)" stroke-width="1.6"/></svg>
        mail@mail.com
      </li>
    </ul>
    <div class="pattern-side" role="img" aria-label="Decorative trail of overlapping outlined circles"></div>
    <p class="tagline">Visualization to Manifestation</p>
    <p class="website">www.website.com</p>
  </section>
</main>
</body>
</html>
```